Professional consulting firm needing a Word document template

I need a Word document template that can be used flexibly for a flyer or brochure of 1 to 3 pages in length. The first page should be designed in a way that it can stand alone as a one-page flyer without a formal cover page. I have attached sample text as a Word document that could be used as the basis for the first 1-2 pages, however I do need three page layouts designed to give flexibility to use as a 3 page booklet. I have attached our brand guidelines, logo, and some stock images that I have previously purchased (they may not all be useful but it gives some options). <br/>The Word document needs to be set up in away that it can easily be edited to accommodate updates to the text, and some variation in the quantity of text on each page. Each page should be able to accommodate a mixture of paragraph text, bullet points, small boxes to call out highlights, one or more images, and some white space to avoid clutter. It should look professional yet engaging and modern.

Font styles to use
Sans Serif

Requirements
Must have
• Must be an editable Microsoft Word document, using the text provided. Must be a layout suitable to use as 1 page, up to 3 pages. Must comply with brand guidelines.

```html
<!DOCTYPE html>
<html lang="en">
<head>
<meta charset="utf-8">
<title>Norvanta – Brochure Page Layouts</title>
<link href="https://fonts.googleapis.com/css2?family=Lato:wght@400;700;900&display=swap" rel="stylesheet">
<style>
  :root{
    --stage:#222222;
    --paper:#ffffff;
    --cyan:#1fb4e2;
    --teal:#3ccfc8;
    --navy:#0f1f2e;
    --ink:#1b1b1b;
    --sky-a:#3b3f6e;
    --sky-b:#c98a7c;
    --ground:#4b4038;
  }
  *{margin:0;padding:0;box-sizing:border-box}
  html,body{width:1200px;height:1200px;overflow:hidden;background:var(--stage)}
  body{position:relative;font-family:"Lato",sans-serif;color:var(--ink)}
  .page{position:absolute;background:var(--paper);overflow:hidden}
  .page--cover{left:196px;top:71px;width:362px;height:507px}
  .page--overview{left:591px;top:71px;width:363px;height:509px}
  .page--details{left:440px;top:616px;width:366px;height:514px}
  .shapes{position:absolute;left:0;top:0;width:100%;height:100%}
  .abs{position:absolute}
  .brand{position:absolute;font-weight:700;color:var(--navy);letter-spacing:.5px;line-height:1}
  .heading-cyan{color:var(--cyan);font-weight:900;line-height:1.1;text-transform:uppercase}
  .heading-dark{color:var(--ink);font-weight:900;line-height:1.1;text-transform:uppercase}
  .body-text{font-size:5.6px;line-height:1.35;color:var(--ink)}
  .body-text p{margin-bottom:4px}
  .body-text b{font-weight:700}

  /* cover */
  .cover-title{left:12px;top:13px;font-size:12.4px}
  .cover-intro{left:12px;top:63px;width:160px}
  .cover-brand{left:234px;top:58px;font-size:18px}
  .cover-sub{left:40px;top:320px;font-size:12.4px}
  .cover-sub-text{left:38px;top:370px;width:130px;font-size:4.9px}
  .cover-contact{left:242px;top:479px;border-left:1.5px solid var(--navy);padding-left:3px;font-size:6px;line-height:1.35}

  /* overview */
  .ov-brand{left:215px;top:150px;font-size:19px}
  .ov-title{left:185px;top:193px;font-size:11.5px}
  .ov-intro{left:22px;top:245px;width:330px;font-size:6px}
  .checklist{position:absolute;list-style:none;font-size:7px;line-height:14.3px}
  .checklist li{display:flex;align-items:center;gap:4px}
  .checklist svg{width:8px;height:8px;flex:none}
  .checklist--left{left:18px;top:280px}
  .checklist--right{left:200px;top:279px}
  .callout{position:absolute;left:17px;top:385px;width:336px;height:62px;background:var(--cyan)}
  .callout-tab{position:absolute;left:0;top:0;height:16px;width:150px;background:var(--navy);color:#fff;font-weight:700;font-size:8.6px;line-height:16px;padding-left:6px;clip-path:polygon(0 0,100% 0,96% 100%,0 100%)}
  .callout-text{position:absolute;left:8px;top:21px;width:315px;color:#fff;font-size:5.8px;line-height:1.4}
  .ov-outro{left:22px;top:457px;width:325px;font-size:5.9px}

  /* details */
  .tab{position:absolute;left:0;color:#fff;font-weight:700;padding-left:16px}
  .tab--teal{top:182px;width:212px;height:29px;background:var(--teal);font-size:9.6px;line-height:1.1;padding-top:3px;clip-path:polygon(0 0,100% 0,96% 100%,0 100%)}
  .tab--cyan{top:264px;width:138px;height:24px;background:var(--cyan);font-size:9.6px;line-height:24px;padding-left:22px;clip-path:polygon(0 0,100% 0,92% 100%,0 100%)}
  .det-benefits{left:16px;top:219px;width:336px;font-size:5.5px}
  .det-involved{left:18px;top:302px;width:334px;font-size:5.3px}
  .det-brand{left:25px;top:483px;font-size:16px}
  .footer-band{position:absolute;left:120px;top:480px;width:246px;height:34px;background:var(--cyan);clip-path:polygon(8% 0,100% 0,100% 100%,0 100%);color:#fff;font-weight:700;font-size:7.2px;line-height:34px;padding-left:29px}
</style>
</head>
<body>

<!-- Page 1: stand-alone flyer / cover -->
<section class="page page--cover">
  <svg class="shapes" viewBox="0 0 362 507" aria-hidden="true">
    <polygon points="238,0 252,0 0,378 0,356" fill="var(--navy)"/>
    <polygon points="362,130 362,507 190,507 110,507" fill="var(--teal)"/>
    <polygon points="362,130 362,250 270,388 218,388" fill="var(--cyan)"/>
    <polygon points="36,296 84,296 80,305 32,305" fill="var(--teal)"/>
    <polygon points="222,296 262,296 256,305 216,305" fill="#8ee3de"/>
  </svg>
  <svg class="shapes" viewBox="0 0 362 507" role="img" aria-label="Photo of railway tracks at sunset with motion-blurred train lights">
    <defs>
      <linearGradient id="railSky" x1="0" y1="0" x2="0" y2="1">
        <stop offset="0" stop-color="var(--sky-a)"/>
        <stop offset=".45" stop-color="var(--sky-b)"/>
        <stop offset=".6" stop-color="#7f7a88"/>
        <stop offset="1" stop-color="var(--ground)"/>
      </linearGradient>
    </defs>
    <polygon points="206,96 362,96 362,118 244,295 68,295" fill="url(#railSky)"/>
  </svg>

  <h1 class="abs heading-cyan cover-title">Lorem ipsum is<br>placeholder text<br>commonly</h1>
  <p class="abs body-text cover-intro">Lorem ipsum dolor sit amet, consectetur adipiscing elit, sed do eiusmod tempor incididunt ut labore et dolore magna aliqua. Ut enim ad minim veniam, quis nostrud exercitation ullamco laboris nisi ut aliquip ex ea commodo consequat. Duis aute irure dolor in reprehenderit in voluptate velit esse cillum dolore eu fugiat nulla pariatur. Excepteur sint occaecat cupidatat non proident, sunt in culpa qui officia deserunt mollit anim id est laborum.</p>
  <div class="brand cover-brand">NORVANTA</div>
  <h2 class="abs heading-dark cover-sub">Lorem ipsum is<br>placeholder text<br>commonly</h2>
  <p class="abs body-text cover-sub-text">Lorem ipsum dolor sit amet, consectetur adipiscing elit, sed do eiusmod tempor incididunt ut labore et dolore magna aliqua. Ut enim ad minim veniam, quis nostrud exercitation ullamco laboris nisi ut aliquip ex ea commodo consequat. Duis aute irure dolor in reprehenderit in voluptate velit esse cillum dolore eu fugiat nulla pariatur. Excepteur sint occaecat cupidatat non proident, sunt in culpa qui officia deserunt mollit anim id est laborum.</p>
  <div class="abs cover-contact">www.norvanta.com.au<br>contact@norvanta.com.au</div>
</section>

<!-- Page 2: project overview -->
<section class="page page--overview">
  <svg class="shapes" viewBox="0 0 363 509" aria-hidden="true">
    <polygon points="0,0 22,0 0,34" fill="var(--teal)"/>
    <polygon points="257,0 293,0 161,207 117,207" fill="var(--teal)"/>
  </svg>
  <svg class="shapes" viewBox="0 0 363 509" role="img" aria-label="Photo of a train driver's cab at dusk with instrument screens and track ahead">
    <defs>
      <linearGradient id="cabView" x1="0" y1="0" x2="0" y2="1">
        <stop offset="0" stop-color="#4a3f63"/>
        <stop offset=".45" stop-color="#8a8aa6"/>
        <stop offset=".65" stop-color="#2a2c36"/>
        <stop offset="1" stop-color="#121318"/>
      </linearGradient>
    </defs>
    <polygon points="33,0 247,0 141,197 0,197 0,60" fill="url(#cabView)"/>
  </svg>

  <div class="brand ov-brand">NORVANTA</div>
  <h1 class="abs heading-cyan ov-title">Train driver competency<br>indicator development<br>project</h1>
  <p class="abs body-text ov-intro">We are commencing an applied research project to develop and test a framework of underlying core competencies for train driver performance. The objective of the project is to identify observable indicators that describe effective performance in the following types of underlying competencies:</p>

  <ul class="checklist checklist--left">
    <li><svg viewBox="0 0 10 10"><path d="M1 5.5 L4 8.5 L9.5 1.5" fill="none" stroke="var(--cyan)" stroke-width="2"/></svg>Application of Procedures</li>
    <li><svg viewBox="0 0 10 10"><path d="M1 5.5 L4 8.5 L9.5 1.5" fill="none" stroke="var(--cyan)" stroke-width="2"/></svg>Communication</li>
    <li><svg viewBox="0 0 10 10"><path d="M1 5.5 L4 8.5 L9.5 1.5" fill="none" stroke="var(--cyan)" stroke-width="2"/></svg>Operation of Tools / Equipment</li>
    <li><svg viewBox="0 0 10 10"><path d="M1 5.5 L4 8.5 L9.5 1.5" fill="none" stroke="var(--cyan)" stroke-width="2"/></svg>Problem Solving and Decision Making</li>
    <li><svg viewBox="0 0 10 10"><path d="M1 5.5 L4 8.5 L9.5 1.5" fill="none" stroke="var(--cyan)" stroke-width="2"/></svg>Route Knowledge</li>
    <li><svg viewBox="0 0 10 10"><path d="M1 5.5 L4 8.5 L9.5 1.5" fill="none" stroke="var(--cyan)" stroke-width="2"/></svg>Self Management</li>
  </ul>
  <ul class="checklist checklist--right">
    <li><svg viewBox="0 0 10 10"><path d="M1 5.5 L4 8.5 L9.5 1.5" fill="none" stroke="var(--cyan)" stroke-width="2"/></svg>Situation Awareness</li>
    <li><svg viewBox="0 0 10 10"><path d="M1 5.5 L4 8.5 L9.5 1.5" fill="none" stroke="var(--cyan)" stroke-width="2"/></svg>System Knowledge</li>
    <li><svg viewBox="0 0 10 10"><path d="M1 5.5 L4 8.5 L9.5 1.5" fill="none" stroke="var(--cyan)" stroke-width="2"/></svg>Teamwork and Leadership</li>
    <li><svg viewBox="0 0 10 10"><path d="M1 5.5 L4 8.5 L9.5 1.5" fill="none" stroke="var(--cyan)" stroke-width="2"/></svg>Train Handling</li>
    <li><svg viewBox="0 0 10 10"><path d="M1 5.5 L4 8.5 L9.5 1.5" fill="none" stroke="var(--cyan)" stroke-width="2"/></svg>Workload Management</li>
  </ul>

  <div class="callout">
    <div class="callout-tab">Underlying Competencies :</div>
    <p class="callout-text">The underpinning knowledge and skills required by a train driver, to perform a range of different tasks effectively. Underlying competencies include both ‘technical’ and ‘non-technical’ skills. They are not specific to one driving task, but help build resilient performance across all tasks, conditions or situations that a driver may encounter.</p>
  </div>

  <p class="abs body-text ov-outro">In contrast to other performance marker systems, the current project aims to include both ‘technical’ and ‘non-technical’ skills in an integrated framework, with substantial input from drivers across the industry, both in passenger and freight operations. The aim is to develop a framework that uses a language that describes performance in a way that is relatable to drivers, trainers, and assessors.</p>
</section>

<!-- Page 3: participation details -->
<section class="page page--details">
  <svg class="shapes" viewBox="0 0 366 514" aria-hidden="true">
    <polygon points="332,0 366,0 366,166 284,166" fill="var(--cyan)"/>
    <polygon points="333,0 337,0 263,184 259,184" fill="var(--teal)"/>
  </svg>
  <svg class="shapes" viewBox="0 0 366 514" role="img" aria-label="Photo of a level crossing at night with stop sign, red warning lights and a blurred passing train">
    <defs>
      <linearGradient id="crossingNight" x1="0" y1="0" x2="0" y2="1">
        <stop offset="0" stop-color="#2b3f8a"/>
        <stop offset=".3" stop-color="#4f6aa0"/>
        <stop offset=".5" stop-color="#6fb6c0"/>
        <stop offset=".7" stop-color="#3b4a7a"/>
        <stop offset="1" stop-color="#2a3560"/>
      </linearGradient>
    </defs>
    <polygon points="0,0 332,0 284,166 0,166" fill="url(#crossingNight)"/>
  </svg>

  <h2 class="tab tab--teal">What are the benefits for participating<br>organisations?</h2>
  <p class="abs body-text det-benefits">All participating rail organisations will receive a copy of the performance indicator framework, which they are free to use or adapt for application within their own operation. A summary report will also be provided, outlining the methodology and aggregated results of the data collection activities. All results will be presented in a de-identified way, to ensure the anonymity of participating organisations and individuals.</p>

  <h2 class="tab tab--cyan">What is involved?</h2>
  <div class="abs body-text det-involved">
    <p>Participating organisations will be invited to provide in-kind support for the following activities during the period April – June 2020 :</p>
    <p><b>Interviews with volunteer Driver participants:</b> individual discussions with our researchers about drivers’ previous experiences, to gather information about expert driving strategies and positive techniques used in normal and abnormal operations.</p>
    <p><b>Initial workshop:</b> a facilitated group workshop to understand the links between underlying competencies and driving tasks, and to understand Drivers’ perceptions of what each underlying competency looks like in practice.</p>
    <p><b>Driver Training Survey:</b> a voluntary survey will be distributed, requesting Driver Trainers’ and Assessors’ views on the importance of underlying competencies in driving performance, and further data about expert strategies and techniques.</p>
    <p><b>Follow-up workshop:</b> a facilitated group workshop to test and refine the performance indicators. Where possible, indicators will be tested through participants providing ratings of a video sample of actual performance, to determine whether multiple raters can distinguish between competency categories.</p>
    <p style="margin-top:7px">It is anticipated that workshops will be run in Brisbane, Sydney and Melbourne. We would appreciate support from participating organisations in providing a workshop venue where possible. Apart from the in-kind support of providing access to personnel and a meeting room, there is no cost associated with participation in the project.</p>
    <p>In addition to the activities involving industry participation, we will also be completing a detailed task analysis and analysing incident reports and other publicly available data, to help inform the development of the framework.</p>
    <p>We look forward to hearing from organisations interested in being part of this landmark project.</p>
  </div>

  <div class="brand det-brand">NORVANTA</div>
  <div class="footer-band">www.norvanta.com.au &nbsp;|&nbsp; contact@norvanta.com.au</div>
</section>

</body>
</html>
```